New business card/stationary for a consulting company

I am looking for a clean and very professional looking business card for my consulting company as well as corresponding stationary. I am uploading our logo. I like simple and powerful for the feel. No graphics but I am open on everything else. Below is my contact information but would like the final to be in a version I can add my employees information into and print. Thank you.

Daniel Whitcombe
dan@ferncrestadvisory.com
2738 North 17th Avenue, Summit Floor, Oak Brook, Illinois 60126
www.ferncrestadvisory.com

Industry/Entity Type

Consulting

Contact Information for Business Card

Daniel Whitcombe
dan@ferncrestadvisory.com
www.ferncrestadvisory.com

Font styles to use
Serif
Sans Serif

Requirements
Must have
• Our logo and the business card details.
Nice to have
• our website www.ferncrestadvisory.com

```html
<!DOCTYPE html>
<html lang="en">
<head>
<meta charset="utf-8">
<title>Ferncrest Advisory — Business Card</title>
<link rel="stylesheet" href="https://fonts.googleapis.com/css2?family=Marcellus&family=Marcellus+SC&family=Mulish:wght@500;800&display=swap">
<style>
  :root {
    --ink: #07088f;
    --paper: #ffffff;
  }
  html, body {
    margin: 0;
    padding: 0;
    width: 1200px;
    height: 686px;
    overflow: hidden;
    background: var(--paper);
  }
  .card {
    position: relative;
    width: 1200px;
    height: 686px;
    background: var(--paper);
    color: var(--ink);
  }
  .brand {
    position: absolute;
    left: 0;
    right: 0;
    top: 180px;
    display: flex;
    justify-content: center;
    align-items: center;
    gap: 22px;
  }
  .brand-square {
    width: 34px;
    height: 34px;
    background: var(--ink);
  }
  .brand-name {
    font-family: "Marcellus", serif;
    font-size: 60px;
    line-height: 1;
    letter-spacing: 4px;
    text-transform: uppercase;
    white-space: nowrap;
  }
  .rule {
    position: absolute;
    left: 0;
    width: 1200px;
    height: 3px;
    background: var(--ink);
  }
  .rule--top { top: 293px; }
  .rule--bottom { top: 599px; }
  .centered {
    position: absolute;
    left: 0;
    right: 0;
    text-align: center;
    white-space: nowrap;
  }
  .person-name {
    top: 366px;
    font-family: "Mulish", sans-serif;
    font-weight: 800;
    font-size: 48px;
    line-height: 1;
  }
  .person-email {
    top: 430px;
    font-family: "Mulish", sans-serif;
    font-weight: 500;
    font-size: 44px;
    line-height: 1;
  }
  .website {
    top: 550px;
    font-family: "Marcellus", serif;
    font-size: 36px;
    line-height: 1;
    letter-spacing: 4px;
    text-transform: uppercase;
  }
  .address {
    top: 618px;
    font-family: "Marcellus SC", serif;
    font-size: 33px;
    line-height: 1;
    letter-spacing: 0.5px;
  }
</style>
</head>
<body>
  <main class="card">
    <header class="brand">
      <span class="brand-square" aria-hidden="true"></span>
      <span class="brand-name">Ferncrest Advisory</span>
    </header>
    <div class="rule rule--top"></div>
    <div class="centered person-name">Daniel Whitcombe</div>
    <div class="centered person-email">dan@ferncrestadvisory.com</div>
    <div class="centered website">www.ferncrestadvisory.com</div>
    <div class="rule rule--bottom"></div>
    <div class="centered address">2738 North 17th Avenue, Summit Floor, Ash Hollow, Illinois 60185</div>
  </main>
</body>
</html>
```